The Pledge a non-fiction book on mindfulness COVER design needed

A non-fiction book about active mindfulness.
The Pledge includes 21 different daily 'dares' which are action based activities to generate positive mindfulness - to become more contented with life.
Based on the teeaching of the New Thought movements of the early 20th century, think The Lantern, Plan and Become Bold.
The book is positive and uplifting. It fits into the self-help / spiritual / health segments. It skews female 40 to 50 year olds.
Think fresh colours like a bold orange or bright green.
What needs to be on the cover:
TITLE: The Pledge
AUTHOR: Marcus Pellworth
BLURB: Get clarity, focus, and a new zest for life by following The Pledge for just 21 days.
Target Market(s)
Women 40-50 english speaking
Industry/Entity Type
Self-help / Health

```html
<!DOCTYPE html>
<html lang="en">
<head>
<meta charset="utf-8">
<title>The Pledge — Book Cover</title>
<link rel="stylesheet" href="https://fonts.googleapis.com/css2?family=Bebas+Neue&display=swap">
<style>
  :root {
    --page-bg: #efece6;
    --cover-red: #ec4137;
    --title-lime: #d5dc2b;
    --title-white: #ffffff;
  }
  * { margin: 0; padding: 0; box-sizing: border-box; }
  html, body {
    width: 1200px;
    height: 1000px;
    overflow: hidden;
    background: var(--page-bg);
  }
  .stage {
    position: relative;
    width: 1200px;
    height: 1000px;
  }
  .book-cover {
    position: absolute;
    left: 280px;
    top: 30px;
    width: 640px;
    height: 940px;
    box-shadow: 0 6px 18px rgba(0, 0, 0, 0.12);
  }
  .book-cover text {
    font-family: "Bebas Neue", "Oswald", sans-serif;
  }
  .cover-field { fill: var(--cover-red); }
  .title-lead { fill: var(--title-white); }
  .title-main { fill: var(--title-lime); }
  .blurb { fill: var(--title-white); }
  .author { fill: var(--title-lime); }
</style>
</head>
<body>
<main class="stage">
  <svg class="book-cover" viewBox="0 0 640 940" width="640" height="940" aria-label="The Pledge by Marcus Pellworth">
    <rect class="cover-field" x="0" y="0" width="640" height="940"/>

    <text class="title-lead" x="345" y="435" font-size="200" textLength="232" lengthAdjust="spacingAndGlyphs">THE</text>
    <text class="title-main" x="70" y="680" font-size="320" textLength="507" lengthAdjust="spacingAndGlyphs">PLEDGE</text>

    <text class="blurb" x="69" y="738" font-size="33" textLength="508" lengthAdjust="spacingAndGlyphs">GET CLARITY, FOCUS, AND A NEW ZEST FOR LIFE</text>
    <text class="blurb" x="79" y="786" font-size="33" textLength="488" lengthAdjust="spacingAndGlyphs">BY FOLLOWING THE PLEDGE FOR JUST 21 DAYS</text>

    <text class="author" x="105" y="895" font-size="68" textLength="430" lengthAdjust="spacingAndGlyphs">MARCUS PELLWORTH</text>
  </svg>
</main>
</body>
</html>
```